Business Cards that are elegant and wow

I want to create and print business cards that represent my brand and stand out from the rest. We want to ensure they stay in our branding and the integrity is not lost. I am happy to look at different shapes like square etc.

It will be printed on very thick cards and will be stylish .

I want to create and print business cards that represent my brand and stand out from the rest. We want to ensure they stay in ur branding and the integrity is not lost. I am happy to look at different shapes like square etc.

Target Market(s)

real estate professionals

Industry/Entity Type

Real Estate

Contact Information for Business Card

Maren Holt
hello@brightfernrealty.com.au
brightfernrealty.com.au
0487 316 252 (SMS)

Colors

Designer to choose colors to be used in the design.

Requirements
Must have
• My logo
• email
• website
• Name
Nice to have
• I like the idea of printing with foil or spot gloss. You want it to stand out in a sea.
Should not have
• I would like you to stay in my colour themes. Don't change the colour of my logo

```html
<!DOCTYPE html>
<html lang="en">
<head>
<meta charset="utf-8">
<title>Bright Fern Realty – Business Card</title>
<link rel="stylesheet" href="https://fonts.googleapis.com/css2?family=Montserrat:wght@500&family=Open+Sans:wght@400&family=Arimo:wght@400&display=swap">
<style>
  :root {
    --backdrop: #e8e5e1;
    --card: #ffffff;
    --cyan: #00c2f3;
    --cyan-light: #63d9f7;
    --pink: #e3319b;
    --ink: #111111;
    --white: #ffffff;
  }
  html, body {
    margin: 0;
    padding: 0;
    width: 1200px;
    height: 1023px;
    overflow: hidden;
    background: var(--backdrop);
  }
  .business-card {
    position: absolute;
    left: 75px;
    top: 211px;
    width: 1050px;
    height: 600px;
    background: var(--card);
    box-shadow: 0 10px 30px rgba(0,0,0,0.15);
    overflow: hidden;
  }
  .brand {
    position: absolute;
    left: 126px;
    top: 92px;
    display: flex;
    align-items: center;
    gap: 22px;
  }
  .brand-circle {
    width: 70px;
    height: 70px;
    border-radius: 50%;
    border: 5px solid var(--cyan);
    box-sizing: border-box;
  }
  .brand-name {
    font-family: 'Montserrat', sans-serif;
    font-weight: 500;
    font-size: 44px;
    letter-spacing: 1px;
    color: var(--cyan);
    line-height: 1;
  }
  .holder-name {
    position: absolute;
    right: 80px;
    top: 100px;
    font-family: 'Arimo', sans-serif;
    font-size: 40px;
    color: var(--ink);
  }
  .rule {
    position: absolute;
    left: 0;
    width: 100%;
    height: 4px;
    background: var(--pink);
  }
  .rule-top { top: 254px; }
  .rule-bottom { top: 436px; }
  .band {
    position: absolute;
    left: 0;
    top: 266px;
    width: 100%;
    height: 162px;
    background: linear-gradient(90deg, var(--cyan-light) 0%, var(--cyan) 45%, var(--cyan) 100%);
  }
  .contact-list {
    position: absolute;
    left: 232px;
    top: 290px;
    margin: 0;
    padding: 0;
    list-style: none;
    font-family: 'Open Sans', sans-serif;
    font-size: 26px;
    color: var(--white);
  }
  .contact-list li {
    display: flex;
    align-items: center;
    gap: 18px;
    height: 40px;
  }
  .contact-icon {
    width: 22px;
    height: 22px;
    flex: none;
  }
</style>
</head>
<body>
  <main class="business-card">
    <div class="brand">
      <div class="brand-circle"></div>
      <span class="brand-name">BRIGHT FERN REALTY</span>
    </div>

    <div class="holder-name">Maren Holt</div>

    <div class="rule rule-top"></div>
    <div class="band"></div>
    <div class="rule rule-bottom"></div>

    <ul class="contact-list">
      <li>
        <svg class="contact-icon" viewBox="0 0 22 22" aria-hidden="true">
          <rect x="1" y="1" width="20" height="20" rx="4" fill="#ffffff"/>
          <rect x="7" y="4" width="8" height="14" rx="1.5" fill="none" stroke="#00c2f3" stroke-width="1.8"/>
        </svg>
        <span>0487 316 252 (SMS)</span>
      </li>
      <li>
        <svg class="contact-icon" viewBox="0 0 22 22" aria-hidden="true">
          <rect x="1" y="1" width="20" height="20" rx="4" fill="#ffffff"/>
          <rect x="4.5" y="6.5" width="13" height="9" fill="none" stroke="#00c2f3" stroke-width="1.6"/>
          <path d="M4.5 6.5 L11 12 L17.5 6.5" fill="none" stroke="#00c2f3" stroke-width="1.6"/>
        </svg>
        <span>hello@brightfernrealty.com.au</span>
      </li>
      <li>
        <svg class="contact-icon" viewBox="0 0 22 22" aria-hidden="true">
          <rect x="1" y="1" width="20" height="20" rx="4" fill="#ffffff"/>
          <circle cx="11" cy="11" r="6.5" fill="none" stroke="#00c2f3" stroke-width="1.6"/>
          <path d="M4.5 11 H17.5 M11 4.5 C8 8 8 14 11 17.5 M11 4.5 C14 8 14 14 11 17.5" fill="none" stroke="#00c2f3" stroke-width="1.3"/>
        </svg>
        <span>brightfernrealty.com.au</span>
      </li>
    </ul>
  </main>
</body>
</html>
```